Business Card Design

We are looking for a double sided business card.

On one side would be our logo

On the Other Side

Martin Kolby
Sales and Marketing

Phone/Text Logo and 530-418-2763
Email Logo and info@plumvalepets.com
Website Logo and www.plumvalepets.com
Facebook Logo and plumvale pets
Instagram Logo and plumvale_pets

Target Market(s)

Pet owners

Contact Information for Business Card

In project description

Requirements
Must have
• Logo

```html
<!DOCTYPE html>
<html lang="en">
<head>
<meta charset="utf-8">
<title>Plumvale Pets – Business Card</title>
<link rel="stylesheet" href="https://fonts.googleapis.com/css2?family=Montserrat:wght@500;600;700&display=swap">
<style>
  :root {
    --stage: #2b2d30;
    --card: #1b1b1c;
    --card-edge: #f39019;
    --accent: #f7a21b;
    --text-light: #f4f4f4;
    --emboss: #262627;
    --emboss-hi: #303031;
  }
  html, body {
    margin: 0;
    width: 1200px;
    height: 811px;
    overflow: hidden;
    background: var(--stage);
    font-family: "Montserrat", sans-serif;
  }
  .stage {
    width: 1200px;
    height: 811px;
    display: flex;
    flex-direction: column;
    align-items: center;
    justify-content: center;
    gap: 40px;
  }
  .card {
    position: relative;
    width: 600px;
    height: 343px;
    background: var(--card);
    border-left: 3px solid var(--card-edge);
    border-bottom: 3px solid var(--card-edge);
    box-shadow: 0 14px 28px rgba(0,0,0,0.45);
    box-sizing: border-box;
  }
  /* front: embossed brand name */
  .card-front {
    display: flex;
    align-items: center;
    justify-content: center;
  }
  .front-brand {
    display: flex;
    flex-direction: column;
    align-items: center;
    gap: 10px;
  }
  .front-brand .brand-name {
    font-weight: 700;
    font-size: 52px;
    letter-spacing: 1px;
    text-transform: uppercase;
    color: var(--emboss-hi);
  }
  .front-brand .brand-url {
    font-weight: 500;
    font-size: 13px;
    letter-spacing: 3px;
    text-transform: uppercase;
    color: var(--emboss-hi);
  }
  /* back: brand + contacts */
  .card-back {
    display: flex;
    align-items: center;
    padding: 0 30px 0 34px;
  }
  .back-brand {
    width: 270px;
    display: flex;
    flex-direction: column;
    align-items: center;
    gap: 8px;
  }
  .back-brand .brand-name {
    font-weight: 700;
    font-size: 34px;
    text-transform: uppercase;
    color: var(--text-light);
    line-height: 1.1;
    text-align: center;
  }
  .back-brand .brand-url {
    font-weight: 600;
    font-size: 10px;
    letter-spacing: 2.5px;
    text-transform: uppercase;
    color: var(--accent);
  }
  .divider {
    width: 2px;
    height: 170px;
    background: var(--card-edge);
    margin: 0 26px 0 12px;
  }
  .contact {
    color: var(--text-light);
  }
  .contact .person-name {
    margin: 0;
    font-weight: 700;
    font-size: 20px;
    color: var(--accent);
  }
  .contact .person-role {
    margin: 2px 0 16px;
    font-weight: 500;
    font-size: 14px;
  }
  .contact-list {
    list-style: none;
    margin: 0;
    padding: 0;
    display: flex;
    flex-direction: column;
    gap: 5px;
    font-size: 14px;
    font-weight: 500;
  }
  .contact-list li {
    display: flex;
    align-items: center;
    gap: 9px;
  }
  .contact-list svg {
    width: 14px;
    height: 14px;
    flex: none;
  }
</style>
</head>
<body>
<main class="stage">
  <section class="card card-front" aria-label="Business card front">
    <div class="front-brand">
      <span class="brand-name">Plumvale Pets</span>
      <span class="brand-url">www.plumvalepets.com</span>
    </div>
  </section>

  <section class="card card-back" aria-label="Business card back">
    <div class="back-brand">
      <span class="brand-name">Plumvale Pets</span>
      <span class="brand-url">www.plumvalepets.com</span>
    </div>
    <div class="divider"></div>
    <div class="contact">
      <h1 class="person-name">Martin Kolby</h1>
      <p class="person-role">Sales and Marketing</p>
      <ul class="contact-list">
        <li>
          <svg viewBox="0 0 24 24" aria-hidden="true"><path fill="#f7a21b" d="M6.6 10.8a15 15 0 0 0 6.6 6.6l2.2-2.2c.3-.3.7-.4 1-.2 1.1.4 2.3.6 3.6.6.6 0 1 .4 1 1V20c0 .6-.4 1-1 1A17 17 0 0 1 3 4c0-.6.4-1 1-1h3.5c.6 0 1 .4 1 1 0 1.3.2 2.5.6 3.6.1.3 0 .7-.2 1z"/></svg>
          530-418-2763
        </li>
        <li>
          <svg viewBox="0 0 24 24" aria-hidden="true"><rect x="2" y="5" width="20" height="14" rx="2" fill="#f7a21b"/><path d="M3 6l9 7 9-7" fill="none" stroke="#1b1b1c" stroke-width="2"/></svg>
          info@plumvalepets.com
        </li>
        <li>
          <svg viewBox="0 0 24 24" aria-hidden="true"><g fill="none" stroke="#f7a21b" stroke-width="2"><circle cx="12" cy="12" r="9"/><ellipse cx="12" cy="12" rx="4" ry="9"/><path d="M3 12h18"/></g></svg>
          www.plumvalepets.com
        </li>
        <li>
          <svg viewBox="0 0 24 24" aria-hidden="true"><circle cx="12" cy="12" r="9" fill="#f7a21b"/></svg>
          plumvale pets
        </li>
        <li>
          <svg viewBox="0 0 24 24" aria-hidden="true"><rect x="3" y="3" width="18" height="18" rx="4" fill="none" stroke="#f7a21b" stroke-width="2.2"/></svg>
          plumvale_pets
        </li>
      </ul>
    </div>
  </section>
</main>
</body>
</html>
```